Fast growing Tech company needs redesign of Veltrana's end user website!

We need to have our login screen, the dashboard, and the one page of the Veltrana site to be redesigned for the end-users. Veltrana is a document hosting service for title companies and real estate law firms. This allows the buyers and sellers to view their closing documents after closing along with many other features that help them out during the closing of their property. More information about what we do can be found on our test site https://qpx.524.sampledraft-host.com/. PLEASE NOTE: THE ABOVE SITE IS NOT THE ONE WE NEED REDONE. The above site is our corporate site that explains our service offering and we thought it would be helpful in providing you a better understanding of our service.
The site that we want to have redesigned is for the end user. THE SITE THAT NEEDS TO BE REDONE ARE THE SCREENSHOTS ATTACHED. We will need the login screen, dashboard, and the one page redesigned.
.
We will just need this in HTML and we will then do the rest for the placeholders for logos, data, mapping etc.
Overall, we want a new, fresh, and modern look for the website and we want the login screen, dashboard and one page website to be consistent in design. Again, these are the three screenshots that are attached.
For the winner, we will most likely need to hire you again for more sites because we have other versions.
Thank you and if any questions, please let us know.
Target Market(s)
This site is for buyer and sellers during the closing process of real estate transaction.

```html
<!DOCTYPE html>
<html lang="en">
<head>
<meta charset="utf-8">
<title>Veltrana – Login</title>
<link rel="stylesheet" href="https://fonts.googleapis.com/css2?family=Lato:ital,wght@0,400;0,700;1,700&display=swap">
<style>
  :root {
    --brand-blue: #1175bd;
    --brand-blue-soft: #dde9f4;
    --text-dark: #333333;
    --text-muted: #555b61;
    --field-border: #8d9094;
    --icon-green: #5a9e3f;
    --page-bg: #ffffff;
  }
  * { box-sizing: border-box; margin: 0; padding: 0; }
  html, body {
    width: 1200px; height: 675px; overflow: hidden;
    background: var(--page-bg);
    font-family: "Lato", Arial, sans-serif;
    color: var(--text-dark);
  }
  .login-page { position: relative; width: 1200px; height: 675px; }

  .hero-photo {
    position: absolute; left: 16px; top: 19px; width: 721px; height: 639px;
    background:
      linear-gradient(180deg, #cfe0ea 0%, #b9cfa0 22%, #5c7a3a 42%, #2c2f2a 58%, #7aa34a 72%, #3a3a38 86%, #2a2a2a 100%);
  }

  .login-panel { position: absolute; left: 785px; top: 0; width: 370px; height: 675px; }

  .brand-name {
    position: absolute; left: 0; top: 38px;
    font-size: 46px; font-weight: 700; color: var(--brand-blue);
    letter-spacing: 0.5px; line-height: 1;
  }

  .welcome { position: absolute; left: 0; top: 190px; font-size: 17px; color: var(--text-dark); }

  .tab {
    position: absolute; top: 232px; height: 50px; border-radius: 6px;
    display: flex; align-items: center; justify-content: center;
    font-size: 18px;
  }
  .tab--active { left: 0; width: 120px; background: var(--brand-blue); color: #fff; }
  .tab--secondary { left: 137px; width: 232px; background: var(--brand-blue-soft); color: var(--text-muted); }

  .field {
    position: absolute; left: 0; width: 369px; height: 45px;
    border: 1px solid var(--field-border); border-radius: 6px;
    display: flex; align-items: center; padding-left: 14px;
    font-size: 13px; color: var(--text-muted);
  }
  .field svg { margin-right: 14px; flex: none; }
  .field--user { top: 316px; }
  .field--password { top: 383px; }

  .submit-button {
    position: absolute; left: 0; top: 471px; width: 369px; height: 45px;
    background: var(--brand-blue); border-radius: 6px; color: #fff;
    display: flex; align-items: center; justify-content: center; font-size: 18px;
  }
  .submit-button svg { position: absolute; right: 20px; top: 14px; }

  .help { position: absolute; left: 0; top: 612px; font-size: 16px; line-height: 28px; color: var(--text-dark); }
  .help a { color: var(--brand-blue); font-weight: 700; font-style: italic; text-decoration: none; }
</style>
</head>
<body>
<main class="login-page">
  <div class="hero-photo" role="img" aria-label="Modern dark timber house with large glass walls among pine trees, green lawn and rocks in front"></div>

  <section class="login-panel">
    <div class="brand-name">Veltrana</div>

    <p class="welcome">Hello, Welcome Back!</p>

    <div class="tab tab--active">Login</div>
    <div class="tab tab--secondary">New User / Account Reset</div>

    <div class="field field--user">
      <svg width="20" height="22" viewBox="0 0 20 22" fill="none" stroke="var(--icon-green)" stroke-width="1.6">
        <circle cx="10" cy="6" r="5"/>
        <ellipse cx="10" cy="17.5" rx="8" ry="3.5"/>
      </svg>
      USBKey or Certificate Number
    </div>

    <div class="field field--password">
      <svg width="22" height="22" viewBox="0 0 22 22" fill="none" stroke="var(--icon-green)" stroke-width="1.6">
        <rect x="1" y="1" width="20" height="20" rx="5"/>
        <circle cx="7.5" cy="11" r="2.5"/>
        <path d="M10 11h7M15 11v2.5M17 11v2"/>
      </svg>
      Password
    </div>

    <div class="submit-button">Submit
      <svg width="24" height="17" viewBox="0 0 24 17" fill="none" stroke="#fff" stroke-width="1.8">
        <path d="M1 8.5h14"/>
        <path d="M12 2l9 6.5-9 6.5z"/>
      </svg>
    </div>

    <p class="help">Need some help?<br>Email us at <a href="mailto:mail@closingfilesuite.com">mail@closingfilesuite.com</a></p>
  </section>
</main>
</body>
</html>
```